I need a business card designed using the logo provided either vertical or horizontal......Quenbury Advisory is an Australian based real estate company that caters for the upper end of the market so the design of the business card "must reflect" the companies image!!
Colour combinations are optional but "must be realistic" and must be able to be accurately useable CMYK colours.
Please consider that any colours used "must be able to be used" and be suitable in following designs for "pull out banner signs" and "real estate signs".
The colours and the font in the attached designs are for example and other combinations are encouraged.
Target Market(s)
The High End of the Australian real estate market
Industry/Entity Type
Business
Contact Information for Business Card
Logo - Business Name - Director + Licensed Real Estate Agent - Mobile Number (Cell Phone) - Business Number - Fax - Email Address - Web address
Requirements
Must have
- Designs and colours (CMYK) that can easily be interpreted by an Australian printer.
Nice to have
- Some alternative ideas on colour and font..........the ones provided are ok and have been provided as an example but I am looking for alternative ideas
Should not have
- Loud, overly bright colours. Designs that do not reflect the professional standards of the business.
- Designs that look good on a computer monitor but can not be re-created on a printing press.............this is most important when it comes to shading etc.

```html
<!DOCTYPE html>
<html lang="en">
<head>
<meta charset="utf-8">
<title>Quenbury Advisory – Business Card</title>
<link href="https://fonts.googleapis.com/css2?family=Exo+2:wght@400;500;600&display=swap" rel="stylesheet">
<style>
  :root {
    --backdrop: #3b3431;
    --card: #151515;
    --gold: #c8912e;
    --ink: #f2f2f2;
    --muted: #d6d6d6;
  }
  * { box-sizing: border-box; margin: 0; padding: 0; }
  html, body { width: 1200px; height: 780px; overflow: hidden; }
  body {
    background: var(--backdrop);
    font-family: "Exo 2", sans-serif;
    position: relative;
  }
  .card {
    position: absolute;
    top: 235px;
    width: 540px;
    height: 310px;
    background: var(--card);
    border-radius: 4px;
    box-shadow: 0 10px 30px rgba(0,0,0,.35);
  }
  .card--front { left: 40px; }
  .card--back { left: 620px; }

  .brand {
    position: absolute;
    display: flex;
    align-items: center;
    gap: 14px;
  }
  .brand__dot {
    width: 22px; height: 22px;
    border-radius: 50%;
    background: var(--gold);
    flex: none;
  }
  .brand__name {
    color: var(--ink);
    font-weight: 500;
    font-size: 24px;
    letter-spacing: 3px;
    text-transform: uppercase;
    white-space: nowrap;
  }
  .card--front .brand { left: 50%; top: 50%; transform: translate(-50%, -50%); }
  .card--back .brand { right: 44px; top: 58px; }
  .card--back .brand__name { font-size: 21px; letter-spacing: 2.5px; }

  .person {
    position: absolute;
    left: 30px;
    top: 150px;
    width: 220px;
    text-align: right;
  }
  .person__name { color: var(--gold); font-weight: 600; font-size: 19px; letter-spacing: .5px; }
  .person__role { color: var(--ink); font-size: 12.5px; margin-top: 2px; }
  .person__address { color: var(--ink); font-size: 13px; line-height: 1.4; margin-top: 10px; }

  .divider {
    position: absolute;
    left: 268px;
    top: 170px;
    width: 1px;
    height: 95px;
    background: var(--muted);
  }

  .contact {
    position: absolute;
    left: 288px;
    top: 176px;
    list-style: none;
  }
  .contact__item {
    display: flex;
    align-items: center;
    gap: 10px;
    color: var(--ink);
    font-size: 14px;
    height: 22px;
    white-space: nowrap;
  }
  .contact__icon {
    width: 15px; height: 15px;
    background: var(--gold);
    border-radius: 2px;
    display: flex; align-items: center; justify-content: center;
    flex: none;
  }
  .contact__icon svg { width: 11px; height: 11px; }
</style>
</head>
<body>

  <section class="card card--front" aria-label="Card front">
    <div class="brand">
      <span class="brand__dot"></span>
      <span class="brand__name">Quenbury Advisory</span>
    </div>
  </section>

  <section class="card card--back" aria-label="Card back">
    <div class="brand">
      <span class="brand__dot"></span>
      <span class="brand__name">Quenbury Advisory</span>
    </div>

    <div class="person">
      <p class="person__name">Marlow Vance</p>
      <p class="person__role">Managing Director</p>
      <p class="person__address">Suite 4, 12 Kestrel Row<br>Mosman, NSW 2088</p>
    </div>

    <span class="divider"></span>

    <ul class="contact">
      <li class="contact__item">
        <span class="contact__icon"><svg viewBox="0 0 12 12"><path d="M3 1.5 L4.8 3.6 L3.9 4.6 Q5 7 7.4 8.1 L8.4 7.2 L10.5 9 L9.4 10.5 Q4.5 10 1.5 2.6 Z" fill="#fff"/></svg></span>
        0400 118 275
      </li>
      <li class="contact__item">
        <span class="contact__icon"><svg viewBox="0 0 12 12"><rect x="3" y="1.5" width="6" height="3" fill="#fff"/><rect x="1.5" y="5" width="9" height="4" rx="1" fill="#fff"/><rect x="3" y="8" width="6" height="2.5" fill="#fff"/></svg></span>
        02 9180 4420
      </li>
      <li class="contact__item">
        <span class="contact__icon"><svg viewBox="0 0 12 12"><rect x="1.5" y="3" width="9" height="6.5" fill="#fff"/><path d="M1.5 3 L6 7 L10.5 3" stroke="#c8912e" stroke-width="1" fill="none"/></svg></span>
        info@quenbury.com.au
      </li>
      <li class="contact__item">
        <span class="contact__icon"><svg viewBox="0 0 12 12"><circle cx="6" cy="6" r="4.3" fill="none" stroke="#fff" stroke-width="1.2"/><ellipse cx="6" cy="6" rx="1.8" ry="4.3" fill="none" stroke="#fff" stroke-width="1"/><path d="M1.7 6 H10.3" stroke="#fff" stroke-width="1"/></svg></span>
        www.quenbury.com.au
      </li>
    </ul>
  </section>

</body>
</html>
```